Redesign of Website

We need an overhaul of our website. I've attached our current logo files. Please visit www.qelvorbis.com for our current website for information about our company. We are looking for the same type of website (information-based only) so no need for any online store, payments, interactive stuff or anything like that...basically looking for a fresh new look! Also please make sure this design will be mobile-friendly. Thanks!

```html
<!DOCTYPE html>
<html lang="en">
<head>
<meta charset="utf-8">
<title>Qelvor Consultants, Inc.</title>
<link href="https://fonts.googleapis.com/css2?family=Montserrat:wght@400;500;600;700&family=Raleway:wght@400;500;600&display=swap" rel="stylesheet">
<style>
:root{
  --navy:#0d2f78;
  --navy-dark:#0a2660;
  --green:#8cc98a;
  --teal:#2e6d7a;
  --ink:#1c1c1c;
  --text:#333;
  --muted:#777;
  --white:#fff;
}
*{box-sizing:border-box;margin:0;padding:0}
html,body{width:1200px;height:3543px;overflow:hidden}
body{position:relative;background:var(--white);font-family:'Raleway',sans-serif;color:var(--text)}
.abs{position:absolute}
.heading{font-family:'Montserrat',sans-serif;font-weight:600;text-transform:uppercase}

/* header */
.site-header{left:0;top:0;width:1200px;height:130px;background:var(--white)}
.brand{font-family:'Montserrat',sans-serif;font-weight:700;color:var(--navy);text-transform:uppercase;line-height:1;white-space:nowrap}
.header-brand{left:110px;top:50px;font-size:24px;letter-spacing:1px}
.contact-chip{display:flex;align-items:center;gap:12px;font-family:'Montserrat',sans-serif;font-size:14px;line-height:20px;color:var(--ink);white-space:nowrap}
.contact-chip b{color:var(--navy);font-weight:600;display:block}
.search{left:870px;top:24px;width:242px;height:42px;border:1px solid #ddd;border-radius:21px;padding:0 0 0 22px;font-size:14px;color:#999;display:flex;align-items:center}
.search .btn{position:absolute;right:6px;top:6px;width:30px;height:30px;border-radius:50%;background:#333;display:flex;align-items:center;justify-content:center}
.main-nav{top:92px;left:480px;display:flex;gap:0;font-family:'Montserrat',sans-serif;font-size:16px;color:var(--ink)}
.main-nav span{margin-right:38px}

/* hero */
.hero{left:0;top:130px;width:1200px;height:583px;background:linear-gradient(100deg,#c8b79a 0%,#8f8a80 35%,#6e7480 60%,#5d6270 100%)}
.hero-title{left:563px;top:283px;font-size:44px;color:var(--white);font-weight:500}
.hero-text{left:567px;top:347px;width:540px;font-size:19px;line-height:44px;color:var(--white);text-align:justify}
.pill{display:flex;align-items:center;justify-content:center;gap:8px;background:var(--navy);color:var(--white);border-radius:28px;font-family:'Montserrat',sans-serif;font-weight:600;font-size:16px}
.hero-btn{left:563px;top:493px;width:197px;height:53px}

/* welcome */
.section-title{width:1200px;left:0;text-align:center;font-size:34px;color:var(--ink)}
.rule{height:3px;background:var(--green)}
.frame-blue{left:93px;top:868px;width:507px;height:375px;background:var(--navy)}
.frame-green{left:120px;top:900px;width:512px;height:370px;background:var(--green)}
.welcome-photo{left:107px;top:883px;width:511px;height:373px;background:linear-gradient(135deg,#7f8fa6 0%,#b7b2a6 45%,#d9c9a8 70%,#8a7a60 100%)}
.welcome-text{left:657px;top:876px;width:440px;font-size:14.5px;line-height:26px;color:#222;text-align:justify}
.welcome-text p{margin-bottom:10px}
.welcome-btn{left:657px;top:1200px;width:199px;height:57px}

/* services */
.services{left:0;top:1342px;width:1200px;height:563px;background:linear-gradient(120deg,#0b3580 0%,#1a4a86 40%,#4d8f86 75%,#8fcb8a 100%)}
.light-title{color:var(--white)}
.intro{width:1200px;left:0;text-align:center;font-size:17px;line-height:37px;color:var(--white)}
.service-card{top:1567px;width:322px;height:258px;border:1px solid rgba(255,255,255,.35);background:rgba(255,255,255,.06);box-shadow:0 4px 14px rgba(0,0,0,.25);text-align:center;color:var(--white);padding-top:22px}
.service-card h3{font-family:'Montserrat',sans-serif;font-weight:700;font-size:21px;line-height:30px;margin-top:10px;text-transform:uppercase}
.service-card p{font-size:12.5px;line-height:25px;margin:8px auto 0;width:240px}
.arrow{top:1680px}

/* team */
.member{top:2120px;width:228px;height:268px}
.member .photo{position:absolute;left:0;top:0;width:228px;height:268px;border:3px solid var(--navy);background:linear-gradient(180deg,#7a8a99 0%,#c7a58c 55%,#54524e 100%)}
.member .bar-top{position:absolute;left:74px;top:-6px;width:80px;height:6px;background:var(--navy)}
.member .bar-l{position:absolute;left:-6px;top:100px;width:6px;height:70px;background:var(--navy)}
.member .bar-r{position:absolute;right:-6px;top:100px;width:6px;height:70px;background:var(--navy)}
.member .caption{position:absolute;left:0;bottom:0;width:228px;height:52px;background:var(--navy);color:var(--white);text-align:center;padding-top:8px}
.member .name{font-family:'Montserrat',sans-serif;font-weight:600;font-size:16px;line-height:20px}
.member .role{font-family:'Montserrat',sans-serif;font-weight:600;font-size:10px;line-height:16px}

/* contact */
.contact{left:0;top:2468px;width:1200px;height:777px;background:linear-gradient(120deg,#0b3580 0%,#1c4a82 40%,#4d8f86 72%,#8fcb8a 100%)}
.info{width:300px;text-align:center;color:var(--white);font-family:'Montserrat',sans-serif;font-weight:600;font-size:17px;line-height:30px}
.info svg{display:block;margin:0 auto 16px}
.field{height:40px;background:var(--white);font-size:12px;color:#555;display:flex;align-items:center;padding-left:18px;gap:6px}
.submit{left:512px;top:3115px;width:178px;height:50px;background:var(--navy-dark);color:var(--white);font-family:'Montserrat',sans-serif;font-weight:600;font-size:17px;display:flex;align-items:center;justify-content:center;gap:8px}

/* footer */
.footer-brand{left:0;width:1200px;top:3318px;text-align:center;font-size:60px;letter-spacing:4px}
.footer-nav{left:0;width:1200px;top:3403px;text-align:center;font-family:'Montserrat',sans-serif;font-weight:600;font-size:15px;color:var(--ink)}
.footer-nav i{font-style:normal;margin:0 10px}
.copy{left:0;width:1200px;top:3446px;text-align:center;font-size:14px;color:var(--muted)}
.socials{left:530px;top:3486px;display:flex;gap:6px}
.socials span{width:32px;height:32px;border:2px solid var(--navy);border-radius:50%}
</style>
</head>
<body>

<header class="abs site-header">
  <div class="abs brand header-brand">Qelvor Consultants</div>
  <div class="abs contact-chip" style="left:495px;top:20px">
    <svg width="42" height="42" viewBox="0 0 42 42"><circle cx="21" cy="21" r="19" fill="none" stroke="#0d2f78" stroke-width="3"/><path d="M14 12c2-1 3 0 4 3s-1 3-1 4c1 3 3 5 6 6 1 0 2-2 4-1s3 2 2 4c-1 2-4 3-7 1-5-3-8-6-10-11-1-3 0-5 2-6z" fill="#0d2f78"/></svg>
    <div><b>Call us:</b>555-014-2290</div>
  </div>
  <div class="abs contact-chip" style="left:675px;top:20px">
    <svg width="44" height="34" viewBox="0 0 48 36"><rect x="2" y="2" width="44" height="32" fill="#0d2f78"/><path d="M2 2l22 18L46 2" fill="none" stroke="#fff" stroke-width="3"/></svg>
    <div><b>Mail us:</b>info@qelvorbis.com</div>
  </div>
  <div class="abs search">Search<span class="btn"><svg width="14" height="14" viewBox="0 0 14 14"><circle cx="6" cy="6" r="4" fill="none" stroke="#fff" stroke-width="2"/><path d="M9 9l4 4" stroke="#fff" stroke-width="2"/></svg></span></div>
  <nav class="abs main-nav"><span>HOME</span><span>ABOUT US</span><span>SERVICES</span><span>OUR TEAM</span><span>OUR BLOG</span><span>CONTACT</span></nav>
</header>

<section class="abs hero" role="img" aria-label="Engineer in hard hat and safety vest reviewing plans at a building construction site"></section>
<h1 class="abs heading hero-title">Plan and Cost Reviews</h1>
<p class="abs hero-text">Expert Analysis Saves Money - Our Plan &amp; Cost Reviews provide lending institutions with expert analysis of new construction projects before loan commitments are made</p>
<div class="abs pill hero-btn"><svg width="13" height="15" viewBox="0 0 13 15"><path d="M0 0h8l5 5v10H0z" fill="#fff"/></svg>READ MORE</div>

<h2 class="abs heading section-title" style="top:790px">Welcome to Qelvor Consultants, Inc.</h2>
<div class="abs rule" style="left:535px;top:846px;width:130px"></div>
<div class="abs frame-blue"></div>
<div class="abs frame-green"></div>
<div class="abs welcome-photo" role="img" aria-label="Team reviewing rolled blueprints on a desk with a hard hat"></div>
<div class="abs welcome-text">
  <p>With over 25 years experience we provide customized and comprehensive inspection services to financial institutions involved in construction and loan management in New York, New Jersey, Pennsylvania and surrounding areas.</p>
  <p>The firm's professional staff bring years of engineering, environmental, building, and real estate experience to work for our clients.</p>
  <p>Qelvor provides our clients with in-depth plan &amp; cost, construction funding, environmental and property condition reports.</p>
</div>
<div class="abs pill welcome-btn"><svg width="13" height="15" viewBox="0 0 13 15"><path d="M0 0h8l5 5v10H0z" fill="#fff"/></svg>READ MORE</div>

<section class="abs services"></section>
<h2 class="abs heading section-title light-title" style="top:1413px">Our Service</h2>
<p class="abs intro" style="top:1467px">Sed ut perspiciatis unde omnis iste natus error sit voluptatem accusantium doloremque laudantium,<br>quae ab illo inventore veritatis et quasi architecto beatae vitae dicta sunt explicabo.</p>
<svg class="abs arrow" style="left:40px" width="36" height="30" viewBox="0 0 36 30"><path d="M34 15H4M16 3L4 15l12 12" fill="none" stroke="#fff" stroke-width="3"/></svg>
<svg class="abs arrow" style="left:1124px" width="36" height="30" viewBox="0 0 36 30"><path d="M2 15h30M20 3l12 12-12 12" fill="none" stroke="#fff" stroke-width="3"/></svg>

<div class="abs service-card" style="left:90px">
  <svg width="70" height="70" viewBox="0 0 70 70" fill="none" stroke="#fff" stroke-width="2.5"><rect x="16" y="8" width="40" height="52"/><circle cx="34" cy="30" r="11"/><path d="M34 30V19M34 30h11M22 46h26M22 52h20"/></svg>
  <h3>Property Condition<br>Reports</h3>
  <p>Sed ut perspiciatis unde omnis iste natus error sit voluptatem accusantium doloremque laudantium, totam rem</p>
</div>
<div class="abs service-card" style="left:438px">
  <svg width="70" height="70" viewBox="0 0 70 70" fill="none" stroke="#fff" stroke-width="2.5"><rect x="12" y="8" width="36" height="52"/><circle cx="30" cy="24" r="9"/><path d="M30 18v12M18 42h24M18 50h18"/><rect x="42" y="40" width="18" height="22"/><path d="M46 46h10M46 52h10"/></svg>
  <h3>Plan &amp; Cost<br>Reviews</h3>
  <p>Sed ut perspiciatis unde omnis iste natus error sit voluptatem accusantium doloremque laudantium, totam rem</p>
</div>
<div class="abs service-card" style="left:788px">
  <svg width="70" height="70" viewBox="0 0 70 70" fill="none" stroke="#fff" stroke-width="2.5"><path d="M20 62V10M14 14h44M20 10l-8 4M50 14v14"/><rect x="44" y="28" width="12" height="8"/><rect x="28" y="40" width="28" height="22"/><path d="M34 46h6M44 46h6M34 54h6M44 54h6"/></svg>
  <h3>Construction Funding<br>Inspections</h3>
  <p>Sed ut perspiciatis unde omnis iste natus error sit voluptatem accusantium doloremque laudantium, totam rem</p>
</div>

<h2 class="abs heading section-title" style="top:1975px;color:var(--navy)">Our Team</h2>
<p class="abs intro" style="top:2022px;color:#222">Sed ut perspiciatis unde omnis iste natus error sit voluptatem accusantium doloremque laudantium,<br>quae ab illo inventore veritatis et quasi architecto beatae vitae dicta sunt explicabo.</p>

<div class="abs member" style="left:95px"><span class="bar-top"></span><span class="bar-l"></span><span class="bar-r"></span><div class="photo" role="img" aria-label="Portrait photo of team member"></div><div class="caption"><div class="name">EVAN CARROW</div><div class="role">PRESIDENT</div></div></div>
<div class="abs member" style="left:357px"><span class="bar-top"></span><span class="bar-l"></span><span class="bar-r"></span><div class="photo" role="img" aria-label="Portrait photo of team member"></div><div class="caption"><div class="name">NEIL CARROW</div><div class="role">CHIEF FINANCIAL OFFICER</div></div></div>
<div class="abs member" style="left:618px"><span class="bar-top"></span><span class="bar-l"></span><span class="bar-r"></span><div class="photo" role="img" aria-label="Portrait photo of team member"></div><div class="caption"><div class="name">DANA MIREL</div><div class="role">DIRECTOR OF OPERATIONS</div></div></div>
<div class="abs member" style="left:879px"><span class="bar-top"></span><span class="bar-l"></span><span class="bar-r"></span><div class="photo" role="img" aria-label="Portrait photo of team member"></div><div class="caption"><div class="name">RORY BLAINE</div><div class="role">PRODUCT DISTRIBUTION MANAGER</div></div></div>

<section class="abs contact"></section>
<h2 class="abs heading section-title light-title" style="top:2540px">Contact Information</h2>
<p class="abs intro" style="top:2590px;font-size:20px">Contact us for more information</p>

<div class="abs info" style="left:153px;top:2656px">
  <svg width="86" height="86" viewBox="0 0 86 86" fill="none" stroke="#fff" stroke-width="2.5"><circle cx="43" cy="43" r="41"/><path d="M43 60s-12-13-12-22a12 12 0 0 1 24 0c0 9-12 22-12 22z"/><circle cx="43" cy="38" r="4"/><path d="M30 60h26"/></svg>
  48 Linden Ridge Rd Suite 110<br>Marlow Township, NJ 07000
</div>
<div class="abs info" style="left:450px;top:2656px">
  <svg width="86" height="86" viewBox="0 0 86 86" fill="none" stroke="#fff" stroke-width="2.5"><circle cx="43" cy="43" r="41"/><path d="M32 26c3-2 5 0 6 4s-2 4-1 6c2 4 5 7 9 9 2 1 3-2 6-1s4 3 3 6c-2 3-6 4-10 2-7-4-12-9-15-16-2-5-1-8 2-10z"/></svg>
  Phone:<br>555-014-2290
</div>
<div class="abs info" style="left:765px;top:2656px">
  <svg width="86" height="86" viewBox="0 0 86 86" fill="none" stroke="#fff" stroke-width="2.5"><circle cx="43" cy="43" r="41"/><rect x="25" y="31" width="36" height="25"/><path d="M25 31l18 14 18-14"/></svg>
  Email:<br>info@qelvorbis.com
</div>

<h2 class="abs heading section-title light-title" style="top:2838px">Contact Us</h2>
<div class="abs field" style="left:162px;top:2898px;width:428px">&#128100; First Name</div>
<div class="abs field" style="left:610px;top:2898px;width:428px">&#128100; Last Name</div>
<div class="abs field" style="left:162px;top:2953px;width:428px">&#9638; Company</div>
<div class="abs field" style="left:162px;top:3008px;width:428px">&#9993; Email Address</div>
<div class="abs field" style="left:162px;top:3063px;width:428px">&#9742; Phone Number</div>
<div class="abs field" style="left:610px;top:2953px;width:428px;height:150px;align-items:flex-start;padding-top:12px">&#9998; Message :</div>
<div class="abs submit"><svg width="18" height="16" viewBox="0 0 18 16"><path d="M0 7L18 0 14 16 9 11 6 15V10L15 2 4 9z" fill="#fff"/></svg>SUBMIT</div>

<div class="abs brand footer-brand">Qelvor Consultants</div>
<nav class="abs footer-nav">HOME<i>|</i>ABOUT US<i>|</i>OUR SERVICES<i>|</i>OUR TEAM<i>|</i>CONTACT US</nav>
<p class="abs copy">© 2019 Company Name &nbsp;All right reserved</p>
<div class="abs socials"><span></span><span></span><span></span><span></span></div>

</body>
</html>
```